White Paper and One-Page Advertisement for TELVAMORE-QX

I need both documents to be better formatted and designed so they look professional, not something someone with mediocre word skills put together. They will go out to 1000s of industry professionals, and they need to look sharp. I need them to have my company's color palate logo, and branding on it similar to how it is now, but better. Please do not change any of the written content, but it can be arranged in any other format you think is better. Smart art and things i've already used can be omitted in favor of better designs. The developer is free to use their creativity. White paper should not be longer than the three pages unless necessary.

Target Market(s)

Life Sciences supply chain professionals

Colors
33b8a4
0592cd
9bcb3c
fbee3e
3277b5

Requirements
Must have
• Must be professional looking and not look like something done in word. Please use the color palate as seen on the documents.
Should not have
• Any changes to the written content.

```html
<!DOCTYPE html>
<html lang="en">
<head>
<meta charset="utf-8">
<title>TELVAMORE-QX — One-Page Advertisement</title>
<link href="https://fonts.googleapis.com/css2?family=Lato:wght@400;700;900&display=swap" rel="stylesheet">
<style>
  :root{
    --ink:#1f2a2e;
    --navy-teal:#0c3446;
    --deep-green:#0a5a4c;
    --heading-teal:#147a68;
    --lime:#9bcb3c;
    --lime-dark:#86b52f;
    --emerald:#0c8c6c;
    --olive:#b3b52a;
    --aqua:#3aafc0;
    --cream:#f4f1c8;
    --panel:#ececec;
    --page:#f7f7f7;
    --photo-warm:#8a5a3a;
    --photo-teal:#2f6f73;
  }
  *{margin:0;padding:0;box-sizing:border-box}
  html,body{width:1020px;height:1200px;overflow:hidden;background:var(--page)}
  body{font-family:'Lato',sans-serif;color:var(--ink);position:relative}

  .top-panel{position:absolute;left:0;top:0;width:1020px;height:600px;
    background:linear-gradient(90deg,#f3f3f3 0%,#ffffff 55%,#e9e9e9 100%)}
  .header{position:absolute;left:0;top:0;width:1020px;height:150px}
  .page-title{position:absolute;left:47px;top:72px;font-size:42px;font-weight:900;color:#fff;letter-spacing:-.3px}
  .site-url{position:absolute;right:40px;top:86px;font-size:24px;font-weight:900;color:var(--navy-teal)}

  .brand{position:absolute;left:690px;top:150px;display:flex;align-items:center;gap:14px}
  .brand-dot{width:46px;height:46px;border-radius:50%;background:var(--lime)}
  .brand-name{font-size:34px;font-weight:900;color:var(--deep-green);letter-spacing:.5px}

  .bullets{position:absolute;left:79px;list-style:none;font-size:17px;line-height:22.5px}
  .bullets li{position:relative;padding-left:56px}
  .bullets li::before{content:"o";position:absolute;left:0;top:0}
  .bullets.bold{font-weight:700;font-size:18px}

  .steps{position:absolute;left:0;top:255px}
  .step-label{position:absolute;width:170px;text-align:center;font-weight:700;font-size:21px;line-height:26px;color:var(--cream);transform:translate(-50%,-50%)}

  .section-title{position:absolute;left:47px;font-size:42px;font-weight:900;color:var(--heading-teal);letter-spacing:-.5px}

  .mission-box{position:absolute;left:56px;top:1049px;width:426px;height:91px;border:2.5px solid var(--heading-teal);border-radius:14px;padding:8px 14px;font-size:12.5px;line-height:15px;color:#222}
  .mission-box p+p{margin-top:15px}

  .photo{position:absolute;left:565px;top:881px;width:426px;height:270px;border-top-left-radius:90px;
    background:linear-gradient(135deg,var(--photo-warm) 0%,#c39a72 40%,var(--photo-teal) 100%)}

  .footer-band{position:absolute;left:0;top:1163px;width:1020px;height:37px;
    background:linear-gradient(90deg,#062a22 0%,var(--deep-green) 50%,#0d7a60 100%)}
</style>
</head>
<body>
  <div class="top-panel"></div>

  <svg class="header" width="1020" height="150" viewBox="0 0 1020 150" aria-hidden="true">
    <defs>
      <linearGradient id="hdr" x1="0" x2="1" y1="0" y2="0">
        <stop offset="0" stop-color="#0c2f40"/>
        <stop offset=".55" stop-color="#0d4a56"/>
        <stop offset="1" stop-color="#0a5a4c"/>
      </linearGradient>
    </defs>
    <rect width="1020" height="150" fill="url(#hdr)"/>
    <path d="M0 0 H640 L380 150 H0Z" fill="#0b2a3a" opacity=".45"/>
    <path d="M0 137 H460 C520 137 540 75 640 70 H1020 V150 H0Z" fill="#ffffff"/>
    <path d="M0 143 H470 C540 143 560 82 660 80 H1020 V150 H0Z" fill="#f3f3f3"/>
    <path d="M525 120 C580 95 610 80 700 78 H1020 V118 H525Z" fill="#9bcb3c"/>
  </svg>
  <h1 class="page-title">Our Platform</h1>
  <div class="site-url">www.telvamoreqx.com</div>

  <div class="brand">
    <span class="brand-dot"></span>
    <span class="brand-name">TELVAMORE-QX</span>
  </div>

  <ul class="bullets" style="top:155px">
    <li>A multi-vendor marketplace for the life science community<br>to transact pre-market and after-market materials and equipment</li>
    <li>Researchers, manufactures, and original suppliers can<br>create an account to buy, sell, or donate materials</li>
  </ul>

  <svg class="steps" width="1020" height="220" viewBox="0 255 1020 220" aria-hidden="true">
    <g fill="none" stroke="#222" stroke-width="2.5" stroke-dasharray="9 7">
      <path d="M62 388 A112 112 0 0 1 284 388"/>
      <path d="M286 345 A112 112 0 0 0 508 345"/>
      <path d="M511 388 A112 112 0 0 1 733 388"/>
      <path d="M735 345 A112 112 0 0 0 958 345"/>
    </g>
    <circle cx="172" cy="366" r="100" fill="#8fc23a"/>
    <circle cx="397" cy="366" r="100" fill="#0c8c6c"/>
    <circle cx="622" cy="366" r="100" fill="#b3b52a"/>
    <circle cx="847" cy="366" r="100" fill="#3aafc0"/>
    <g fill="#fff" opacity=".12">
      <ellipse cx="172" cy="320" rx="80" ry="45"/>
      <ellipse cx="397" cy="320" rx="80" ry="45"/>
      <ellipse cx="622" cy="320" rx="80" ry="45"/>
      <ellipse cx="847" cy="320" rx="80" ry="45"/>
    </g>
  </svg>
  <div class="step-label" style="left:172px;top:369px">Authentication and terms of quality</div>
  <div class="step-label" style="left:397px;top:369px">Set up<br>store</div>
  <div class="step-label" style="left:622px;top:369px">Seamlessly trasnact and request for information</div>
  <div class="step-label" style="left:847px;top:369px">Check out<br>and sign</div>

  <ul class="bullets" style="top:478px">
    <li>Part 11 compliant signature and authentication</li>
    <li>Leverages industry auditing skills to facilitate compliant and transparent transactions</li>
    <li>Some of the best and industry vendors and software used</li>
  </ul>

  <h2 class="section-title" style="top:555px">Benefits</h2>
  <ul class="bullets" style="top:620px">
    <li>Reduce write-offs by selling excess and obsolete materials, equipment, spare parts, etc.</li>
    <li>Buy quality materials at a reduced price.</li>
    <li>Market materials if an original supplier</li>
    <li>Donate material to researchers</li>
    <li>Acquire donated materials</li>
    <li>Collaborate and consort to reduce supply chain risk such as mutual aid agreements,<br>joint supplier audits, etc.</li>
  </ul>

  <h2 class="section-title" style="top:782px">Our Promise</h2>
  <ul class="bullets" style="top:847px">
    <li>A greener, more cost-efficient, and quality driven supply chain<br>througha collaborativelife sciences marketplace.</li>
  </ul>

  <h2 class="section-title" style="top:899px">Contact Us</h2>
  <ul class="bullets bold" style="top:964px">
    <li>Visit www.telvamoreqx.com</li>
    <li>Email info@telvamoreqx.com</li>
    <li>Read our white paper</li>
  </ul>

  <div class="mission-box">
    <p>TELVAMORE-QX aspires to change the waste and risk paradigm<br>in the life science industry.</p>
    <p>We strive to make companies better stewards of their dollars<br>and our environment to transfer benefit to them...THE PATIENT</p>
  </div>

  <div class="photo" role="img" aria-label="Photograph of people smiling together during a traditional ceremony"></div>

  <div class="footer-band"></div>
</body>
</html>
```